Company document Header needed

Using our current logo, I need a Designer to create a header for use on our company documents. This header will include our business address, phone, fax, website address
Updates

Project Deadline Extended
Reason: Dear designers, I am so pleased with the many different options that have been presented, that I wish to purchase several of them from a few different designers. I will get with the art bazaar folks and figure out what is the best way to do this. In the meantime, I am extending the deadline to allow for a few edits such as our phone number and such. thanks to you all for your excellent work. MB

Designers,

Please take a look and edit any of your submissions that have incorrect info on them:  the correct info is below:

Business name is: Tor Vale, Inc.

website address is:  www.torvale-example.com

Office #:  (855) TorVale2  

Fax#:  (858) 561-2947  (generally I do not intend to need this on any materials unless it balances a look)

email:  info@torvale-example.com

Address:  612 Harbor Rd. suite 2240  San Diego, CA  92113

Thanks!

Industry/Entity Type

Business

```html
<!DOCTYPE html>
<html lang="en">
<head>
<meta charset="utf-8">
<title>Tor Vale, Inc. — Letterhead</title>
<link href="https://fonts.googleapis.com/css2?family=PT+Sans+Narrow:wght@400;700&display=swap" rel="stylesheet">
<style>
  :root {
    --backdrop: #3a3a3a;
    --paper: #ffffff;
    --brand-blue: #0e5a8c;
    --brand-blue-dark: #0a4a76;
    --band-blue: #e6f3fc;
    --text-grey: #6b6b6b;
    --link-blue: #1a5f8f;
  }
  html, body {
    margin: 0;
    padding: 0;
    width: 1200px;
    height: 907px;
    overflow: hidden;
    background: var(--backdrop);
  }
  .letterhead {
    position: absolute;
    left: 307px;
    top: 40px;
    width: 496px;
    height: 699px;
    background: var(--paper);
    transform: scale(1.17);
    transform-origin: top left;
    box-shadow: 0 2px 10px rgba(0,0,0,0.45);
    font-family: "PT Sans Narrow", "Arial Narrow", sans-serif;
  }
  .header-band {
    position: absolute;
    left: 61px;
    top: 94px;
    width: 435px;
    height: 52px;
    background: linear-gradient(90deg, var(--band-blue) 0%, rgba(230,243,252,0.6) 100%);
  }
  .brand-block {
    position: absolute;
    left: 206px;
    top: 0;
    width: 84px;
    height: 87px;
    background: linear-gradient(180deg, var(--brand-blue) 0%, var(--brand-blue-dark) 100%);
    display: flex;
    align-items: flex-end;
    justify-content: center;
  }
  .brand-name {
    margin: 0 0 9px;
    color: var(--paper);
    font-weight: 700;
    font-size: 15px;
    line-height: 1;
  }
  .contact {
    position: absolute;
    left: 304px;
    top: 22px;
    font-size: 7px;
    line-height: 8px;
    font-weight: 700;
    font-style: normal;
    color: var(--text-grey);
  }
  .contact p { margin: 0; }
  .contact .website {
    margin-top: 5px;
    color: var(--link-blue);
  }
</style>
</head>
<body>
  <main class="letterhead">
    <div class="header-band" role="img" aria-label="Soft pale blue band across the header"></div>

    <div class="brand-block">
      <p class="brand-name">TOR VALE</p>
    </div>

    <address class="contact">
      <p>612 Harbor Rd. suite 2240</p>
      <p>San Diego, CA 92113</p>
      <p>Phone: 858-561-2947</p>
      <p class="website">www.torvale-example.com</p>
    </address>
  </main>
</body>
</html>
```